Purpose, Mission, and Values Poster Update

Corvane Field Laboratories, a Testing, Inspection, and Certification company in the Atlanta area, needs an updated PMV poster. Looking to update graphics and presentation, moving away from current design. Want to carry over company logo, colors (you can include additional blues in the design beyond what is mentioned in the brand guidelines as the previous design did), and messaging (see attachments).

We would also like a companion poster, using the same design language, that shows our goals for leads and won opportunities. Want to carry over logo, colors, and messaging from original, except for this one we want the leads goal to be 115 instead of 85.

Both posters need to be 6000w x 7200h at 300ppi, CMYK. We want to move away from the cartoony, corporate clipart sort of look that the current design has, as new leadership doesn't like the aesthetic.

Target Market(s)

Internal - group of engineers, chemists, scientists, and other technical personnel

Industry/Entity Type

TIC (Testing, Inspection, Certification)

Font styles to use
Serif
Sans Serif

Colors
0054AA
0677BA
7BADD7
CADEEF
E8F1F8

Requirements
Must have
• For both: CMYK colors for printing, 6000w x 7200h at 300ppi for poster sizing leads, company logo; for PMV poster: phrasing of purpose, mission, and values statements preserved; for ring the bell poster: leads goal updated to 115, opportunities goal unchanged at 25
Should not have
• Corporate clipart, cartoon characters

```html
<!DOCTYPE html>
<html lang="en">
<head>
<meta charset="utf-8">
<title>Corvane Field Laboratories — Purpose, Mission and Values Poster</title>
<link rel="stylesheet" href="https://fonts.googleapis.com/css2?family=Roboto:wght@400;500;700;900&display=swap">
<style>
  :root {
    --stage: #e6eaf0;
    --navy: #0b1f45;
    --navy-mid: #143a72;
    --ink: #1d2b44;
    --brand-blue: #0054AA;
    --mid-blue: #1f6dbb;
    --bright-blue: #2ba4e8;
    --sky: #7BADD7;
    --pale: #CADEEF;
    --mist: #E8F1F8;
    --white: #ffffff;
  }
  html, body {
    margin: 0;
    padding: 0;
    width: 1200px;
    height: 2514px;
    overflow: hidden;
    background: var(--stage);
  }
  .poster {
    position: absolute;
    left: 50px;
    top: 597px;
    width: 1100px;
    height: 1320px;
    box-shadow: 0 14px 40px rgba(11, 31, 69, 0.25);
    background: var(--white);
  }
  .poster svg { display: block; width: 100%; height: 100%; }
  .poster text { font-family: "Roboto", Arial, sans-serif; }
  .heading { font-weight: 700; }
  .purpose-title { fill: var(--navy); font-size: 46px; }
  .purpose-line { fill: var(--mid-blue); font-size: 28px; font-weight: 500; }
  .mission-title { fill: var(--bright-blue); font-size: 45px; }
  .mission-line { fill: var(--white); font-size: 27px; font-weight: 500; }
  .values-title { fill: var(--bright-blue); font-size: 46px; }
  .value-name { fill: #1a4d98; font-size: 20px; font-weight: 700; }
  .value-text { fill: var(--ink); font-size: 14.5px; font-weight: 400; }
  .brand-name { fill: var(--navy); font-size: 17px; font-weight: 500; }
  .value-icon-disc { fill: var(--navy); }
  .value-icon-ring { fill: none; stroke: var(--bright-blue); stroke-width: 7; }
  .value-icon-glyph { fill: none; stroke: var(--white); stroke-width: 2; stroke-linecap: round; stroke-linejoin: round; }
</style>
</head>
<body>
<div class="poster">
  <svg viewBox="0 0 908 1090" xmlns="http://www.w3.org/2000/svg">
    <defs>
      <linearGradient id="sky-band" x1="0" y1="1" x2="1" y2="0">
        <stop offset="0" stop-color="#dfe9f3"/>
        <stop offset="0.5" stop-color="#8db8df"/>
        <stop offset="1" stop-color="#2f7fc4"/>
      </linearGradient>
      <linearGradient id="plant-tones" x1="0" y1="0" x2="1" y2="1">
        <stop offset="0" stop-color="#9fb0bf"/>
        <stop offset="0.6" stop-color="#7d8a94"/>
        <stop offset="1" stop-color="#b9c6d2" stop-opacity="0.6"/>
      </linearGradient>
      <linearGradient id="navy-band" x1="0" y1="0" x2="1" y2="0">
        <stop offset="0" stop-color="var(--navy-mid)"/>
        <stop offset="1" stop-color="var(--navy)"/>
      </linearGradient>
      <linearGradient id="lab-tones" x1="0" y1="0" x2="560" y2="0" gradientUnits="userSpaceOnUse">
        <stop offset="0" stop-color="#5fb1c4"/>
        <stop offset="0.55" stop-color="#3f89ad" stop-opacity="0.85"/>
        <stop offset="1" stop-color="#143a72" stop-opacity="0"/>
      </linearGradient>
      <linearGradient id="team-tones" x1="0" y1="0" x2="1" y2="0">
        <stop offset="0" stop-color="#c3cad4"/>
        <stop offset="0.6" stop-color="#dfe3e9"/>
        <stop offset="1" stop-color="#ffffff" stop-opacity="0"/>
      </linearGradient>
      <linearGradient id="stripe-fade" x1="330" y1="0" x2="908" y2="0" gradientUnits="userSpaceOnUse">
        <stop offset="0" stop-color="#ffffff" stop-opacity="0"/>
        <stop offset="0.55" stop-color="var(--pale)"/>
        <stop offset="1" stop-color="var(--bright-blue)"/>
      </linearGradient>
    </defs>

    <!-- base -->
    <rect class="poster-ground" width="908" height="1090" fill="var(--white)"/>

    <!-- top sky band -->
    <polygon class="sky-band" points="0,0 908,0 908,69 0,400" fill="url(#sky-band)"/>

    <!-- industrial plant photo area -->
    <polygon class="photo-plant" role="img" aria-label="Photo of an industrial processing tower with steel stairways and pipework"
      points="0,0 400,0 400,296 0,442" fill="url(#plant-tones)"/>

    <!-- team photo area, faded -->
    <rect class="photo-team" role="img" aria-label="Faded photo of inspection staff in safety gear walking on site"
      x="0" y="680" width="360" height="410" fill="url(#team-tones)"/>

    <!-- mission navy band -->
    <polygon class="mission-band" points="0,400 908,69 908,322 0,653" fill="url(#navy-band)"/>

    <!-- lab photo area -->
    <polygon class="photo-lab" role="img" aria-label="Photo of scientists in lab coats working with samples and a monitor in a laboratory"
      points="0,442 560,238 560,493 0,697" fill="url(#lab-tones)"/>

    <!-- diagonal stripes -->
    <g class="value-stripes" fill="url(#stripe-fade)">
      <polygon points="330,655 908,444 908,456 330,667"/>
      <polygon points="330,689 908,478 908,490 330,701"/>
      <polygon points="330,723 908,512 908,524 330,735"/>
      <polygon points="330,757 908,546 908,558 330,769"/>
      <polygon points="330,791 908,580 908,592 330,803"/>
      <polygon points="330,825 908,614 908,626 330,837"/>
      <polygon points="330,859 908,648 908,660 330,871"/>
      <polygon points="330,893 908,682 908,694 330,705" opacity="0"/>
    </g>

    <!-- purpose -->
    <g class="purpose" transform="rotate(-20 367 217)">
      <text class="heading purpose-title" x="367" y="217">OUR PURPOSE</text>
      <text class="purpose-line" x="384" y="252">Create a safe and reliable world</text>
    </g>

    <!-- mission -->
    <g class="mission" transform="rotate(-20 474 327)">
      <text class="heading mission-title" x="474" y="327">OUR MISSION</text>
      <text class="mission-line">
        <tspan x="490" y="368">Deliver assurance through</tspan>
        <tspan x="490" y="406">precise technical and</tspan>
        <tspan x="490" y="444">professional services</tspan>
      </text>
    </g>

    <!-- values -->
    <g class="values" transform="rotate(-20 159 704)">
      <text class="heading values-title" x="159" y="704">OUR VALUES</text>
      <g class="value-list" transform="translate(180 742)">
        <text class="value-name" x="0" y="0">Keep People First</text>
        <text class="value-text" x="8" y="19">Foster a collaborative and inclusive environment for team members’ growth</text>
        <text class="value-name" x="0" y="69">Deliver Service Excellence</text>
        <text class="value-text" x="8" y="88">Provide best-in-class experiences for our clients</text>
        <text class="value-name" x="0" y="138">Think Global, Act Local</text>
        <text class="value-text" x="8" y="157">Utilize our combined expertise and knowledge to deliver when and where</text>
        <text class="value-name" x="0" y="207">Create Value</text>
        <text class="value-text" x="8" y="226">Work efficiently and effectively to deliver quality results in complex environments</text>
        <text class="value-name" x="0" y="276">Do What’s Right</text>
        <text class="value-text">
          <tspan x="8" y="295">Hold ourselves accountable to the highest safety, professional and</tspan>
          <tspan x="8" y="313">personal standards</tspan>
        </text>
      </g>
    </g>

    <!-- value icons -->
    <g class="value-icons">
      <path class="value-icon-ring" d="M131,737 A30,30 0 0 0 131,797 M166,861 A30,30 0 0 1 166,801 M185,864 A30,30 0 0 0 185,924 M217,988 A30,30 0 0 1 217,928 M236,992 A30,30 0 0 0 236,1052"/>
      <path class="value-icon-ring" d="M131,797 C150,800 160,800 166,801 M166,861 C175,862 180,863 185,864 M185,924 C200,926 210,927 217,928 M217,988 C225,989 230,990 236,992"/>
      <circle class="value-icon-disc" cx="131" cy="767" r="24"/>
      <circle class="value-icon-disc" cx="166" cy="831" r="24"/>
      <circle class="value-icon-disc" cx="185" cy="894" r="24"/>
      <circle class="value-icon-disc" cx="217" cy="958" r="24"/>
      <circle class="value-icon-disc" cx="236" cy="1022" r="24"/>
      <g class="value-icon-glyph">
        <circle cx="126" cy="762" r="4"/><circle cx="137" cy="762" r="4"/>
        <path d="M119,776 q7,-8 14,0 M130,776 q7,-8 14,0"/>
        <path d="M166,821 l3,6 6,1 -4.5,4 1,6 -5.5,-3 -5.5,3 1,-6 -4.5,-4 6,-1 z"/>
        <circle cx="185" cy="894" r="10"/><path d="M175,894 h20 M185,884 q-6,10 0,20 q6,-10 0,-20"/>
        <path d="M207,954 l5,-6 h10 l5,6 -10,12 z M207,954 h20"/>
        <path d="M228,1022 l6,6 11,-12"/>
      </g>
    </g>

    <!-- brand -->
    <g class="brand">
      <rect x="614" y="1000" width="16" height="16" fill="var(--navy)"/>
      <text class="brand-name" x="844" y="1014" text-anchor="end">Corvane Field Laboratories</text>
    </g>
  </svg>
</div>
</body>
</html>
```